Business Card Design for a technology company

Our current business card is outdated and stale.

We need a new look and one soon.

We're a telematics (GPS tracking) company based in Australia. Our audiences are transport and logistics company.

Target Market(s)

1. Transport and Logistics Companies
2. Food and Beverage Manufacturers
3. Concrete Businesses

Industry/Entity Type

Logistics

Contact Information for Business Card

Lumen Rove

Font styles to use
Sans Serif

Colors
3276b5
0255a3
85acd3
cfdeed
ffffff

Requirements
Must have
• Logo
• "Premium Suppliers of Real Time Temperature Tracking"
• Contact Name
• Business Title
• Address
• Telephone
• Mobile
• Email
• Website URL
Nice to have
• Visual representation of tracking or maps.
Should not have
• Image of a satellite as currently shown

```html
<!DOCTYPE html>
<html lang="en">
<head>
<meta charset="utf-8">
<title>Lumen Rove Business Card</title>
<link href="https://fonts.googleapis.com/css2?family=Open+Sans:wght@400;600;700&display=swap" rel="stylesheet">
<style>
  :root {
    --backdrop: #3b3430;
    --card-white: #ffffff;
    --brand-blue: #0255a3;
    --brand-mid: #3276b5;
    --brand-light: #85acd3;
    --brand-pale: #cfdeed;
    --ink: #2e2e2e;
    --ink-soft: #666666;
    --rule: #8a8a8a;
  }
  * { margin: 0; padding: 0; box-sizing: border-box; }
  html, body {
    width: 1200px; height: 844px; overflow: hidden;
    background: var(--backdrop);
    font-family: "Open Sans", sans-serif;
  }
  .stage {
    position: relative; width: 1200px; height: 844px;
    display: flex; align-items: center; justify-content: center; gap: 40px;
  }
  .card {
    position: relative; width: 540px; height: 309px;
    box-shadow: 0 10px 30px rgba(0,0,0,0.45);
  }
  .card-front { background: var(--card-white); color: var(--ink); }
  .card-back {
    background: linear-gradient(160deg, var(--brand-mid) 0%, var(--brand-blue) 100%);
    color: var(--card-white);
    display: flex; flex-direction: column; align-items: center; justify-content: center;
  }
  .wordmark {
    display: flex; align-items: center; gap: 10px;
    font-weight: 700; letter-spacing: -0.5px; white-space: nowrap;
  }
  .wordmark-dot { border-radius: 50%; flex: none; }
  .card-front .wordmark {
    position: absolute; top: 34px; right: 38px;
    font-size: 38px; color: var(--brand-blue);
  }
  .card-front .wordmark-dot { width: 18px; height: 18px; background: var(--brand-blue); }
  .card-back .wordmark { font-size: 50px; color: var(--card-white); }
  .card-back .wordmark-dot { width: 22px; height: 22px; background: var(--card-white); }
  .tagline {
    margin-top: 36px; font-size: 10.5px; letter-spacing: 0.6px;
    text-transform: uppercase; color: var(--brand-pale);
  }
  .rule { position: absolute; left: 32px; right: 32px; height: 1px; background: var(--rule); }
  .rule-top { top: 104px; }
  .rule-mid { top: 218px; }
  .person { position: absolute; left: 32px; top: 124px; }
  .person-name { font-size: 22px; font-weight: 400; color: var(--brand-blue); line-height: 1.1; }
  .person-title { font-size: 14px; color: var(--ink-soft); margin-top: 2px; }
  .address { position: absolute; left: 32px; top: 188px; font-size: 14px; color: var(--ink); }
  .contacts { position: absolute; left: 32px; top: 230px; font-size: 13.5px; color: var(--ink); line-height: 1.55; }
  .contacts .label { color: var(--brand-blue); }
  .contacts .web { color: var(--brand-blue); margin-left: 8px; }
  .contacts .gap { margin-left: 8px; }
</style>
</head>
<body>
  <main class="stage">
    <section class="card card-front" aria-label="Business card front">
      <div class="wordmark"><span class="wordmark-dot"></span>Lumen Rove</div>
      <div class="rule rule-top"></div>
      <div class="person">
        <p class="person-name">Marcus Hale</p>
        <p class="person-title">Managing Director</p>
      </div>
      <p class="address">12345, Address Goes Here Country Name, 123456.</p>
      <div class="rule rule-mid"></div>
      <div class="contacts">
        <p><span class="label">T:</span>(044) 123 456 789<span class="gap"><span class="label">F:</span>(044) 123456789</span><span class="gap"><span class="label">M:</span>(044)123456789</span></p>
        <p><span class="label">E:</span>info@youremail.com<span class="web">www.yourweb.com</span></p>
      </div>
    </section>
    <section class="card card-back" aria-label="Business card back">
      <div class="wordmark"><span class="wordmark-dot"></span>Lumen Rove</div>
      <p class="tagline">Premium Suppliers of Real Time Temperature Tracking</p>
    </section>
  </main>
</body>
</html>
```